Flyer Design Project

Lanterns of Yore is a new collaborative of non-profit historical sites in the Greater Boston area. We're promoting the soft launch of our website by hosting open houses at each of the sites on September 21. We need a flyer to post up at each of the sites.

I have more print design needs to follow, and would really like to have a consistent look, so I intend to directly invite the winning designer to more projects.

Industry/Entity Type

Non-Profit

Requirements
Must have
• The flyer must be one page and be delivered as two files in Microsoft Publisher OR Microsoft Word. One file is for an 8 1/2 x 11 and one is as an 11 x 17 (same design, just scaled larger to fit the bigger paper).

It must have the Lanterns of Yore Logo (attached), and this text (attached) and use black font.

Any color that is not black or white must be chosen from these colors-but don't feel you have to use all of them:

Lanterns of Yore Website Colors

poppy red
c 0
m 93
y 87
k 0
web FF3333

nectarine
c 0
m 54
y 74
k 0
web FF9966

monaco blue

c 100
m 79
y 28
k 12
web 003366

tender shoots
c 30
m 0
y 89
k 0
web CCCC33

emerald
c 80
m 11
y 56
k 0
web 009999

african violet
c 28
m 44
y 0
k 0

web CC99CC

sunflower
c 10
m 33
y 99
k 0
web FF9933

lemon zest
c 4
m 13
y 77
k 0
web FFCC66

Nice to have
• Text and images with in the flyer should be large, simple and clear-as easy to see and read when the entire flyer is viewed on a mobile phone or from a distance as possible.

```html
<!DOCTYPE html>
<html lang="en">
<head>
<meta charset="utf-8">
<title>Lanterns of Yore – Open House Flyer</title>
<link rel="stylesheet" href="https://fonts.googleapis.com/css2?family=Anton&family=Questrial&family=Montserrat:wght@700&display=swap">
<style>
  :root {
    --lemon: #f6d35b;
    --violet: #b995c8;
    --monaco: #1d4e89;
    --poppy: #ff3333;
    --nectarine: #ff9966;
    --shoots: #bcd84a;
    --emerald: #009999;
    --ink: #111111;
    --white: #ffffff;
    --ribbon: #9a6fa8;
    --ribbon-dark: #6e4a7c;
  }
  html, body {
    margin: 0;
    padding: 0;
    width: 953px;
    height: 1200px;
    overflow: hidden;
    background: var(--lemon);
  }
  .flyer {
    position: relative;
    width: 953px;
    height: 1200px;
    overflow: hidden;
    background: var(--lemon);
    font-family: "Questrial", sans-serif;
  }
  .backdrop {
    position: absolute;
    inset: 0;
  }
  .brand-name {
    position: absolute;
    left: 558px;
    top: 34px;
    margin: 0;
    font-family: "Questrial", sans-serif;
    font-weight: 400;
    font-size: 86px;
    line-height: 0.98;
    color: var(--monaco);
  }
  .eras {
    position: absolute;
    left: -219px;
    top: 166px;
    width: 500px;
    margin: 0;
    padding: 0;
    list-style: none;
    text-align: right;
    transform-origin: top right;
    transform: rotate(-41deg);
    font-family: "Anton", sans-serif;
    font-size: 50px;
    line-height: 46px;
    color: var(--poppy);
    text-transform: uppercase;
    white-space: nowrap;
  }
  .event-date {
    position: absolute;
    left: 442px;
    top: 330px;
    margin: 0;
    white-space: nowrap;
    transform-origin: top left;
    transform: rotate(44deg);
    font-family: "Anton", sans-serif;
    font-weight: 400;
    font-size: 57px;
    line-height: 1;
    letter-spacing: 3px;
    color: var(--emerald);
    text-transform: uppercase;
  }
  .intro {
    position: absolute;
    left: 37px;
    top: 628px;
    margin: 0;
    white-space: nowrap;
    font-size: 20px;
    line-height: 20.5px;
    letter-spacing: 0.2px;
    color: var(--ink);
  }
  .partners-heading {
    position: absolute;
    left: 37px;
    top: 820px;
    margin: 0;
    font-family: "Montserrat", sans-serif;
    font-weight: 700;
    font-size: 17px;
    color: var(--monaco);
    text-transform: uppercase;
  }
  .partners {
    position: absolute;
    left: 37px;
    top: 860px;
    margin: 0;
    padding: 0;
    list-style: none;
    font-size: 19px;
    line-height: 20px;
    color: var(--ink);
    white-space: nowrap;
  }
  .partners-featured {
    position: absolute;
    left: 37px;
    top: 1097px;
    margin: 0;
    padding: 0;
    list-style: none;
    font-family: "Montserrat", sans-serif;
    font-weight: 700;
    font-size: 17px;
    line-height: 22px;
    color: var(--monaco);
    text-transform: uppercase;
    white-space: nowrap;
  }
  .highlights {
    position: absolute;
    left: 680px;
    top: 932px;
    width: 240px;
    height: 260px;
  }
  .highlights-shape {
    position: absolute;
    inset: 0;
  }
  .highlights-text {
    position: absolute;
    left: 8px;
    top: 22px;
    width: 200px;
    margin: 0;
    transform: rotate(-8deg);
    font-family: "Anton", sans-serif;
    font-size: 30px;
    line-height: 1;
    text-align: center;
    color: var(--white);
  }
</style>
</head>
<body>
<main class="flyer">
  <svg class="backdrop" width="953" height="1200" viewBox="0 0 953 1200" aria-hidden="true">
    <defs>
      <radialGradient id="steel" cx="0.35" cy="0.25" r="0.9">
        <stop offset="0" stop-color="#bdbdbd"/>
        <stop offset="1" stop-color="#6a6a6a"/>
      </radialGradient>
    </defs>
    <polygon class="violet-corner" points="0,0 394,0 0,363" fill="var(--violet)"/>
    <line x1="394" y1="0" x2="0" y2="363" stroke="var(--monaco)" stroke-width="6"/>
    <polygon class="steel-field" points="394,0 953,0 953,795 264,122" fill="url(#steel)"/>
    <polygon class="shoots-wedge" points="530,194 953,655 953,795 435,290" fill="var(--shoots)"/>
    <line x1="264" y1="122" x2="953" y2="795" stroke="var(--nectarine)" stroke-width="7"/>
  </svg>

  <h1 class="brand-name">Lanterns<br>of Yore</h1>

  <ul class="eras">
    <li>Columbus</li>
    <li>Pilgrims</li>
    <li>Revolution</li>
    <li>Civil War</li>
    <li>Industrialization</li>
  </ul>

  <h2 class="event-date">Saturday, September 21</h2>

  <p class="intro">You know the history. But do you know the stories?<br>Have you found how YOU are connected to the places<br>and lives of the people who’ve shaped our world, our<br>country, our state, and your life today? Find out by<br>exploring some of Massachusetts’ treasured historical<br>gems—you’ll be surprised by the wealth you discover.<br>For hours, directions, and discount/prize passes learn<br>more at www.lanternsofyore.org</p>

  <h3 class="partners-heading">Participating Organizations</h3>
  <ul class="partners">
    <li>Harbor Ridge at Whitcombe Estate</li>
    <li>"Meetinghouse of the Founders" Old First Parish (Unitarian) of Linden</li>
    <li>Ashgrove Memorial Library</li>
    <li>Elena Marsh Dance Theatre's Home at Old Fairhaven Baptist Church</li>
    <li>Pritchard's Boat Shop and Museum</li>
    <li>Mount Larkin Cemetery</li>
    <li>Heritage Museum of Black History: Harbor Campus</li>
    <li>Heritage Museum of Black History: Island Campus</li>
    <li>Monument to the First Settlers</li>
    <li>Old Mast Meeting House</li>
  </ul>
  <ul class="partners-featured">
    <li>The Seabright Park Carousel</li>
    <li>Silas Thorne House</li>
    <li>The Kessler Shul, Bayport's Center for Jewish Culture</li>
  </ul>

  <aside class="highlights">
    <svg class="highlights-shape" width="240" height="260" viewBox="0 0 240 260" aria-hidden="true">
      <polygon points="150,200 232,240 200,262 120,230" fill="var(--ribbon-dark)"/>
      <polygon points="5,0 215,10 200,180 130,178 155,240 10,250" fill="var(--ribbon)"/>
      <polygon points="130,178 200,180 155,240" fill="var(--ribbon-dark)"/>
    </svg>
    <p class="highlights-text">Special Tours, Games, Prizes, and Children’s Activities!</p>
  </aside>
</main>
</body>
</html>
```